Roof Plumbing Company needs simple, modern business card using the attached logo and below details:

Dean Halloway
Summit Gutters Pty Ltd
ABN: 58 214 937 062
Phone: 0417 286 531
Email: summitgutters@mailbrook.com
Website: summitgutters.com.au

For all of your metal roof plumbing requirements contact Summit Gutters for an obligation free quote - no job too big or to small!

Industry/Entity Type

Business

Contact Information for Business Card

Dean Halloway
Summit Gutters Pty Ltd
ABN 58 214 937 062
0417 286 531
summitgutters@mailbrook.com
summitgutters.com.au

Requirements
Must have
• Bright eye catching design, professional look

```html
<!DOCTYPE html>
<html lang="en">
<head>
<meta charset="utf-8">
<title>Summit Gutters Pty Ltd – Business Card</title>
<link rel="stylesheet" href="https://fonts.googleapis.com/css2?family=Arimo:wght@400;700&family=Open+Sans:wght@400&display=swap">
<style>
  :root {
    --brand-red: #e8383b;
    --charcoal: #3a3a3a;
    --ink: #2b2b2b;
    --paper: #ffffff;
  }
  * { margin: 0; padding: 0; box-sizing: border-box; }
  html, body {
    width: 1200px;
    height: 686px;
    overflow: hidden;
    background: var(--paper);
  }
  .card {
    position: relative;
    width: 1200px;
    height: 686px;
    background: var(--paper);
    overflow: hidden;
  }
  .top-band {
    position: absolute;
    left: 0; top: 0;
    width: 1200px; height: 10px;
    background: var(--brand-red);
  }
  .brand {
    position: absolute;
    left: 91px; top: 160px;
    display: flex;
    align-items: center;
    gap: 14px;
  }
  .brand-square {
    width: 30px; height: 30px;
    background: var(--brand-red);
  }
  .brand-name {
    font-family: "Arimo", sans-serif;
    font-weight: 700;
    font-size: 38px;
    line-height: 44px;
    color: var(--brand-red);
    white-space: nowrap;
  }
  .tagline {
    position: absolute;
    left: 493px; top: 160px;
    font-family: "Arimo", sans-serif;
    font-size: 41px;
    color: var(--ink);
    white-space: nowrap;
    letter-spacing: -0.3px;
  }
  .tagline strong { font-weight: 700; }
  .tagline span { font-weight: 400; }
  .contact-panel {
    position: absolute;
    left: 0; top: 369px;
    width: 1200px; height: 317px;
  }
  .contact-list {
    position: absolute;
    left: 73px; top: 369px;
    width: 700px; height: 317px;
    font-family: "Open Sans", sans-serif;
    font-size: 24px;
    line-height: 32px;
    color: var(--paper);
    list-style: none;
  }
  .contact-row {
    position: absolute;
    left: 0;
    display: flex;
    white-space: nowrap;
  }
  .contact-label { width: 146px; flex: none; }
  .row-call    { top: 47px; }
  .row-email   { top: 88px; }
  .row-web     { top: 140px; }
  .row-address { top: 190px; }
</style>
</head>
<body>
<div class="card">
  <div class="top-band"></div>

  <div class="brand">
    <div class="brand-square"></div>
    <div class="brand-name">Summit Gutters</div>
  </div>

  <p class="tagline"><strong>NO JOB TOO BIG OR TO</strong> <span>SMALL!</span></p>

  <svg class="contact-panel" width="1200" height="317" viewBox="0 0 1200 317" aria-hidden="true">
    <path fill="var(--charcoal)" d="M0 0 H465 C530 0 555 30 580 70 C600 100 620 105 660 105 H1000 C1060 105 1075 60 1095 35 C1115 10 1135 0 1165 0 H1200 V317 H0 Z"/>
  </svg>

  <ul class="contact-list">
    <li class="contact-row row-call"><span class="contact-label">Call :-</span><span>0417 286 531</span></li>
    <li class="contact-row row-email"><span class="contact-label">E-Mail :-</span><span>summitgutters@mailbrook.com</span></li>
    <li class="contact-row row-web"><span class="contact-label">Website :-</span><span>summitgutters.com.au</span></li>
    <li class="contact-row row-address"><span class="contact-label">Address :-</span><span>Dean Halloway, Summit Gutters Pty Ltd,<br>ABN 58 214 937 062</span></li>
  </ul>
</div>
</body>
</html>
```